Placing my newer logo on my existing business card

I have a business card that I had you guys do years ago, then I changed my logo, I love both my business card and my logo. The challenge is both my logo and my business card are very similar in color. So I'm not sure how to make my logo stand out.

Sick

```html
<!DOCTYPE html>
<html lang="en">
<head>
<meta charset="utf-8">
<title>Larkspur Metabolic Health – Business Card</title>
<link href="https://fonts.googleapis.com/css2?family=Crimson+Text:wght@400;600;700&display=swap" rel="stylesheet">
<style>
  :root{
    --rust:#a04a35;
    --teal:#84a6a9;
    --teal-text:#7b9ca1;
    --paper:#ffffff;
    --backdrop:#808080;
  }
  *{box-sizing:border-box;margin:0;padding:0}
  html,body{width:890px;height:1200px;overflow:hidden}
  body{background:var(--backdrop);font-family:"Crimson Text",Georgia,serif;position:relative}
  .card{position:absolute;top:258px;width:390px;height:683px;background:var(--paper);overflow:hidden}
  .card--front{left:43px}
  .card--back{left:457px}
  .card svg.shapes{position:absolute;inset:0;width:100%;height:100%}
  .abs{position:absolute}

  /* front */
  .brand-mark{left:50%;top:44px;width:52px;height:52px;margin-left:-26px;border-radius:50%;background:var(--teal)}
  .brand-name{left:0;right:0;top:116px;text-align:center;color:var(--rust);font-size:27px;font-weight:600;line-height:1}
  .rule{width:2px;background:var(--rust);left:43px}
  .person{left:43px;top:303px}
  .person__name{color:var(--rust);font-size:30px;font-weight:600;line-height:1}
  .person__title{color:var(--rust);font-size:19px;line-height:1.2}
  .contact{left:38px;display:flex;align-items:center;gap:7px;font-size:15px;color:var(--teal-text)}
  .contact svg{width:12px;height:12px;flex:none}
  .contact--address{color:var(--rust)}
  .footer-url{left:0;right:0;top:641px;text-align:center;color:#fff;font-size:21px;font-weight:700;letter-spacing:1.5px}

  /* back */
  .conditions-title{left:0;right:0;top:28px;text-align:center;color:var(--rust);font-size:25px;font-weight:600;line-height:1.15}
  .condition{border-left:1.5px solid var(--teal-text);padding-left:5px;color:var(--teal-text);font-size:15px;line-height:22px}
  .condition--accent{border-color:var(--rust);color:var(--rust)}
  .col-l{left:36px}
  .col-r{left:222px}
  .back-url{left:0;right:0;top:568px;text-align:center;color:var(--rust);font-size:16px}
  .call{left:0;right:0;top:640px;text-align:center;color:#fff;font-size:23px;font-weight:700;letter-spacing:1px}
</style>
</head>
<body>

<section class="card card--front" aria-label="Card front">
  <svg class="shapes" viewBox="0 0 390 683" preserveAspectRatio="none" aria-hidden="true">
    <path d="M0 0 H135 C75 8 30 30 0 62 Z" fill="var(--rust)"/>
    <path d="M0 617 C90 624 260 640 330 600 C360 582 380 560 390 540 V683 H0 Z" fill="var(--teal)"/>
  </svg>

  <div class="abs brand-mark"></div>
  <div class="abs brand-name">Larkspur Metabolic Health</div>

  <div class="abs rule" style="top:172px;height:102px"></div>

  <div class="abs person">
    <div class="person__name">Marla Hendricks</div>
    <div class="person__title">Director</div>
  </div>

  <div class="abs rule" style="top:370px;height:46px"></div>

  <div class="abs contact" style="top:423px">
    <svg viewBox="0 0 12 12"><circle cx="6" cy="6" r="6" fill="var(--teal-text)"/><path d="M4 3.2l1 1.6-.6.6c.4.8 1 1.4 1.8 1.8l.6-.6 1.6 1-.6 1.2C5.6 8.6 3.4 6.4 3.2 4z" fill="#fff"/></svg>
    (555) 014-2286
  </div>
  <div class="abs contact" style="top:447px">
    <svg viewBox="0 0 12 12"><circle cx="6" cy="6" r="6" fill="var(--teal-text)"/><rect x="3.5" y="3.5" width="5" height="5" fill="#fff"/></svg>
    (555) 014-2287
  </div>

  <div class="abs rule" style="top:482px;height:52px"></div>

  <div class="abs contact contact--address" style="top:540px">
    <svg viewBox="0 0 12 12"><circle cx="6" cy="6" r="6" fill="var(--rust)"/><path d="M6 2.6a2 2 0 0 1 2 2c0 1.5-2 4-2 4s-2-2.5-2-4a2 2 0 0 1 2-2z" fill="#fff"/></svg>
    1420 alder ave ste#5 riverton ut 84000
  </div>

  <div class="abs footer-url">larkspurhealth.com</div>
</section>

<section class="card card--back" aria-label="Card back">
  <svg class="shapes" viewBox="0 0 390 683" preserveAspectRatio="none" aria-hidden="true">
    <path d="M0 0 H135 C75 8 30 30 0 62 Z" fill="var(--rust)"/>
    <path d="M0 617 C120 610 300 620 360 560 C378 540 386 520 390 515 V683 H0 Z" fill="var(--teal)"/>
  </svg>

  <h1 class="abs conditions-title">Conditions we address for<br>women and men</h1>

  <div class="abs condition col-l" style="top:122px">PCOS<br>Hysterectomy</div>
  <div class="abs condition col-r" style="top:122px">Pre-Diabetes<br>Abdominal Obesity</div>

  <div class="abs condition col-l" style="top:184px">Type-II Diabetes<br>Insulin Resistance</div>
  <div class="abs condition col-r" style="top:184px">High Triglycerides<br>High Blood Pressure</div>

  <div class="abs condition condition--accent col-l" style="top:271px">Hypothyroid<br>Underactive Thyroid</div>
  <div class="abs condition condition--accent col-r" style="top:271px">High Cholesterol<br>Gestational Diabetes</div>

  <div class="abs condition condition--accent col-l" style="top:340px">Fibromyalgia<br>Chronic Fatigue</div>
  <div class="abs condition condition--accent col-r" style="top:340px">Epstein Bar<br>Infertility</div>

  <div class="abs condition col-l" style="top:424px">Chronic Headache<br>&amp; Migraines</div>
  <div class="abs condition col-r" style="top:424px">Infertility Drugs<br>Anti-Depression<br>Medications</div>

  <div class="abs condition col-l" style="top:491px">Hypertension<br>Elevated Fasting Glucose</div>

  <div class="abs back-url">www.larkspurhealth.com</div>
  <div class="abs call">Call Today!: (555)014-2286</div>
</section>

</body>
</html>
```